Bright Path Mission- a non profit locin TZ , east Africa. Needing to attract donors.

A flyer for donors /potential partners. showing what their giving has accomplished this year. An Encouraging way to say thank you at the same time informing the partner of the amazing things God is doing with their generous, faithful giving. We will need to print/email. Thank you for considering this project. Your efforts help in educating and feeding 225 street children, providing a safe haven and trade school for hundreds of women and abused teenagers, medical ship on the longest lake in the world going into unreached people groups, a Bible College Training up pastors to plant churches all over TZ, Congo, Burundi and beyond, youth and children’s kids clubs and youth camps. These are the main areas of bright path mission. Bible college, primary school, trade schools, youth camps/kids clubs. We need help in making sure readers will be drawn to seeing/reading more which leads to donations without overwhelming with too much info. HELP! I can tell you about Jesus I have even authored 7 books, but making s flyer that makes sense it out of my wheelhouse. Again, thank you.
Updates

I do not want longer I need quicker and paid for a 3 day quote. All pictures and logo are on our website. I have tried to send pictures but they won’t send. Please look at. Www.brightpathmissiontz.org

Target Market(s)

Professional adults, large companies, donors

Industry/Entity Type

Non profit missionary Bright Path Mission in Tanzania, Congo, USA and soon to be Canada.

Requirements
Must have
• Color professional pictures, feel good, exciting want to be apart of what God is doing
Nice to have
• Glossy trifold
Should not have
• Fly in the face, guilt feeling, animals in Africa

```html
<!DOCTYPE html>
<html lang="en">
<head>
<meta charset="utf-8">
<title>Bright Path Mission – Trifold</title>
<link href="https://fonts.googleapis.com/css2?family=Montserrat:wght@500;700;800&family=Open+Sans:wght@400;600;700&display=swap" rel="stylesheet">
<style>
:root{
  --green:#1f9a3e;
  --green-dark:#177a30;
  --yellow:#f3e500;
  --cream:#fbf6cf;
  --ink:#1b1b1b;
  --white:#ffffff;
  --bg:#eceeea;
}
*{box-sizing:border-box;margin:0;padding:0}
html,body{width:1200px;height:2732px;overflow:hidden;background:var(--bg)}
body{position:relative;font-family:"Open Sans",Arial,sans-serif;color:var(--ink)}
.spread{position:absolute;left:30px;width:1140px;height:880px;display:flex;overflow:hidden;box-shadow:0 4px 18px rgba(0,0,0,.12)}
.spread--outside{top:40px;background:var(--white)}
.spread--inside{top:970px;background:var(--cream)}
.panel{position:relative;width:380px;height:100%;overflow:hidden}
.heading{font-family:"Montserrat",Arial,sans-serif;font-weight:800;line-height:1.05}
.label{font-family:"Montserrat",Arial,sans-serif;font-weight:700;font-size:15px;letter-spacing:.5px;text-transform:uppercase}
.body-copy{font-size:11.5px;line-height:1.55;margin-bottom:10px}
.photo{position:absolute}
.wordmark{display:flex;align-items:center;gap:8px;font-family:"Montserrat",Arial,sans-serif;font-weight:800;font-size:15px;color:var(--green);text-transform:uppercase;letter-spacing:.5px}
.wordmark .dot{width:14px;height:14px;border-radius:50%;background:var(--green)}

/* outside: back panel */
.panel--mission{background:var(--green);color:var(--white);padding:46px 34px}
.panel--mission .label{color:var(--yellow);margin-bottom:14px}
.mission-quote{font-family:"Montserrat",Arial,sans-serif;font-weight:700;font-size:31px;line-height:1.2;margin-top:40px}
.mission-quote em{font-style:normal;color:var(--yellow)}
.mission-ref{text-align:right;font-size:11px;margin-top:14px}

/* outside: donation panel */
.panel--donate{padding:48px 34px}
.panel--donate .heading{font-size:36px;color:var(--green);margin-bottom:20px}
.panel--donate .heading span{color:var(--ink)}
.panel--donate .tax{font-size:11.5px;font-weight:700;color:var(--green);margin:6px 0 18px}
.contact{font-size:11.5px;line-height:1.6}
.contact .web{color:var(--green);font-weight:600}
.panel--donate .photo{left:0;bottom:0;width:380px;height:300px}

/* outside: cover */
.panel--cover .wordmark{position:absolute;top:58px;left:42px}
.cover-title{position:absolute;right:34px;top:120px;text-align:right;font-size:40px;color:var(--green)}
.cover-title span{color:var(--ink)}
.panel--cover .photo{left:0;bottom:0;width:380px;height:560px}

/* inside */
.panel--inside{padding:60px 32px}
.inside-title{font-size:38px;color:var(--green);margin-bottom:22px}
.inside-title span{color:var(--ink)}
.section-title{font-size:34px;color:var(--green);margin:18px 0 16px}
.section-title span{color:var(--ink)}
.panel--inside .label{color:var(--green);margin:6px 0 10px}
.site{position:absolute;bottom:34px;right:32px;font-size:11.5px;font-weight:600;color:var(--green)}
.shape{position:absolute}
</style>
</head>
<body>

<!-- OUTSIDE SPREAD -->
<section class="spread spread--outside">
  <div class="panel panel--mission">
    <h3 class="label">Micro-Businesses</h3>
    <p class="body-copy">Little by little, women are finding their own footing through our small business training. Sewing, tailoring and bookkeeping classes give mothers a skill that feeds a family.</p>
    <p class="body-copy">Graduates leave with tools, a plan and a circle of friends who pray with them, so every shilling earned becomes a step toward lasting change.</p>
    <p class="body-copy">Your giving buys machines, pays teachers and opens the door for another class of women this year.</p>
    <p class="mission-quote">“To bring hope to the nations through the knowledge of <em>Jesus Christ</em> and the <em>Word of God</em>.”</p>
    <p class="mission-ref">Matt. 28:19</p>
  </div>

  <div class="panel panel--donate">
    <h2 class="heading">How Your <span>Donation</span> Helps</h2>
    <p class="body-copy">Your faithful gifts feed and educate street children, train pastors to plant churches, carry medical care across the lake and give young people a place to belong. Every gift, large or small, joins what God is already doing.</p>
    <p class="tax">Bright Path Mission is a 501(c)3 non-profit organization. Federal Tax ID 00-0000000</p>
    <div class="wordmark"><span class="dot"></span>Bright Path Mission</div>
    <div class="contact" style="margin-top:12px">
      <p>P.O. Box 4410, Mwanza, Tanzania</p>
      <p>info@brightpathmissiontz.org</p>
      <p class="web">Www.brightpathmissiontz.org</p>
    </div>
    <div class="photo" role="img" aria-label="Photo of a group of children and teachers gathered together" style="background:linear-gradient(160deg,#8a6b4f,#4a3527 70%,#2e241d)"></div>
    <svg class="shape" style="left:0;bottom:270px" width="380" height="60" viewBox="0 0 380 60"><polygon points="0,60 380,0 380,60" fill="#ffffff"/></svg>
  </div>

  <div class="panel panel--cover">
    <svg class="shape" style="left:0;top:0" width="380" height="330" viewBox="0 0 380 330">
      <polygon points="0,0 120,0 0,90" fill="var(--green)"/>
      <polygon points="380,200 380,330 0,330 0,300" fill="var(--yellow)"/>
    </svg>
    <div class="wordmark"><span class="dot"></span>Bright Path Mission</div>
    <h1 class="heading cover-title">Bring<br>Smile to<br><span>East Africa</span><br>Together</h1>
    <div class="photo" role="img" aria-label="Photo of smiling school children in East Africa" style="background:linear-gradient(170deg,#b48a62,#6a4a33 60%,#3a2a20);clip-path:polygon(0 20%,100% 0,100% 100%,0 100%)"></div>
    <svg class="shape" style="left:0;bottom:0" width="380" height="90" viewBox="0 0 380 90"><polygon points="0,90 0,20 160,90" fill="var(--green)"/><polygon points="380,90 380,30 260,90" fill="var(--yellow)"/></svg>
  </div>
</section>

<!-- INSIDE SPREAD -->
<section class="spread spread--inside">
  <div class="panel panel--inside">
    <svg class="shape" style="left:0;top:0" width="120" height="44" viewBox="0 0 120 44"><polygon points="0,0 120,0 0,44" fill="var(--green)"/></svg>
    <h2 class="heading inside-title">How Do You Bring Hope <span>To A Nation?</span></h2>
    <p class="body-copy">There are so many things that can and need to be done in Tanzania, one of the poorest regions in the world. However, we believe it starts with education, and not just a secular education, though that is necessary. The only way to bring hope and lasting change in the whole nation is to teach people about Jesus.</p>
    <p class="body-copy">One is to raise up a new generation that will become godly influencers. There is also a need to educate pastors. Those who are responsible for equipping the Church for the work of ministry. Both ends of the spectrum matter because our hearts do.</p>
    <p class="body-copy">Through our Primary School, children are growing up with an excellent education and a strong relationship with Jesus, so they can lead with wisdom and compassion.</p>
    <svg class="shape" style="left:0;bottom:0" width="90" height="70" viewBox="0 0 90 70"><polygon points="0,70 0,0 90,70" fill="var(--yellow)"/></svg>
  </div>

  <div class="panel panel--inside">
    <p class="body-copy">Jesus. They are already becoming godly influencers in their families and communities, carrying hope into every home they visit. Through our Bible College, pastors are trained on how to study and teach the Word so that many of our graduates go on to plant churches.</p>
    <h2 class="heading section-title">How We <span>Serve?</span></h2>
    <h3 class="label">Education</h3>
    <p class="body-copy">Our vision is to raise up a generation of godly influencers. These are young people who are firmly grounded in their relationship with Jesus Christ. They have received the best education, enabling them to take up positions of influence in every area of their nation.</p>
    <p class="body-copy">At the other end of the spectrum, we felt a call to equip the current leaders of the local churches by forming a Bible College.</p>
    <p class="body-copy">Today pastors are being trained in the Word of God, how to study and how to teach. Many of our graduates have gone on to plant churches and start other ministries.</p>
  </div>

  <div class="panel panel--inside">
    <p class="body-copy">to plant churches and start other ministries that serve their communities.</p>
    <h3 class="label">Kid's Clubs</h3>
    <p class="body-copy">Kid's Clubs started as an outreach to children who survive on the streets. During the 2 hour weekly gathering, the children receive food, play games, and learn something from the Word of God.</p>
    <p class="body-copy">This ministry has grown from 11 kids and 2 leaders in the first week, to over 160 kids and more than 15 leaders in 8 different locations, reaching around 225 children on Lake Victoria.</p>
    <p class="body-copy">We hold annual summer camps for youth to refresh and recruit new leaders to the program. We also hold kid's camps to teach and encourage those children who have been a part of Kid's Clubs.</p>
    <h3 class="label" style="margin-top:18px">Village Outreaches</h3>
    <p class="body-copy">The outreach can consist of many different parts, such as seeking out candidates for the Bible College, setting up new Kid's Clubs, a variety of medical training and services, seminars, Jesus film at night, and door-to-door evangelism.</p>
    <p class="site">Www.brightpathmissiontz.org</p>
    <svg class="shape" style="right:0;bottom:0" width="110" height="50" viewBox="0 0 110 50"><polygon points="110,0 110,50 0,50" fill="var(--green)"/></svg>
  </div>
</section>

</body>
</html>
```